Create a Eye Catching Flyerr for my online business

I would like an eye catching flyer with the relevant content for my business.

This flyer is to advertise my online business and the call to action is to get Butchers to sign up to my online site to start selling their products.

the flyer must be eye catching, each to understand, easy to read and relevant to the audience being local butcher shops.

Attached is the marketing packs with all the required information about the business The flyer must not be too long, but the front page must be catching and want the audience to read more. It must very direct, targeted and focused on the audience

It mus be duplicate sides

Reason: need a little more time for review

Industry/Entity Type

Marketing

Font styles to use
Serif
Sans Serif

Colors
9bcb3b
ffffff
fee18a
fac994
f37122
f78f20
ffc214

```html
<!DOCTYPE html>
<html lang="en">
<head>
<meta charset="utf-8">
<title>Prime Cuts Market – Brochure</title>
<link href="https://fonts.googleapis.com/css2?family=Arimo:wght@400;700&family=Oswald:wght@400;500&display=swap" rel="stylesheet">
<style>
  :root{
    --green:#66a12b;
    --green-light:#9bcb3b;
    --white:#ffffff;
    --cream:#fee18a;
    --peach:#fac994;
    --orange:#f37122;
    --orange-light:#f78f20;
    --yellow:#ffc214;
    --ink:#111111;
    --stage:#5d6469;
    --social:#2d7dc0;
  }
  *{margin:0;padding:0;box-sizing:border-box}
  html,body{width:1200px;height:819px;overflow:hidden}
  body{background:var(--stage);font-family:"Arimo",Arial,sans-serif;position:relative}
  .brochure{position:absolute;left:30px;top:40px;width:1140px;height:738px;display:flex}
  .panel{position:relative;width:570px;height:738px;overflow:hidden}

  /* Back panel */
  .back{background:var(--white)}
  .back__top{position:absolute;left:0;top:0;width:570px;height:368px;background:var(--green)}
  .back__intro{position:absolute;left:66px;top:56px;width:440px;color:var(--white);font-size:16px;line-height:20px}
  .back__intro p{margin-bottom:9px}
  .back__photo{position:absolute;left:42px;top:228px;width:300px;height:220px;border-radius:40px 60px 30px 30px;
    background:radial-gradient(ellipse at 45% 55%,#c8393a 0%,#a3282b 45%,#6b8f3a 80%,rgba(102,161,43,0) 100%)}
  .brand-mark{position:absolute;left:140px;top:507px;width:80px;height:80px;border-radius:50%;background:var(--green-light);
    display:flex;align-items:center;justify-content:center;text-align:center;color:var(--white);font-weight:700;font-size:12px;line-height:14px}
  .contact{position:absolute;left:244px;top:518px;width:310px}
  .contact__label{font-size:18px;line-height:23px;color:var(--ink)}
  .contact__url{font-size:23px;font-weight:700;color:var(--orange);margin-top:14px;white-space:nowrap}
  .contact__social{display:flex;gap:6px;margin-top:10px}
  .contact__social span{width:34px;height:34px;border-radius:4px;background:var(--social)}
  .back__stripe{position:absolute;left:0;bottom:0;width:570px;height:28px;display:flex}
  .back__stripe span{height:100%}

  /* Cover panel */
  .cover{background:var(--orange)}
  .cover svg{position:absolute;left:0;top:0}
  .cover__title{position:absolute;left:0;top:92px;width:570px;text-align:center;font-family:"Oswald","Arial Narrow",sans-serif;font-weight:400;
    font-size:46px;color:var(--white);letter-spacing:0.5px;text-shadow:1px 2px 3px rgba(0,0,0,.35)}
  .cover__url{position:absolute;left:0;top:166px;width:570px;text-align:center;color:var(--white);font-size:18px}
  .cover__logo{position:absolute;left:184px;top:221px;width:200px;height:200px;border-radius:50%;background:var(--green-light);
    box-shadow:0 0 30px 18px rgba(255,255,255,.85);display:flex;align-items:center;justify-content:center;text-align:center;
    color:var(--white);font-weight:700;font-size:26px;line-height:30px}
</style>
</head>
<body>
<main class="brochure">
  <section class="panel back">
    <div class="back__top"></div>
    <div class="back__intro">
      <p>If you are interested in joining the revolution, the process is very simple.</p>
      <p>Simply send an email to the address below notifying us of that you are interested in signing up along with the package you are interested in. We will contact you with a Insertion form for you to complete.</p>
      <p>In no time you will be ready and advertising online.</p>
    </div>
    <div class="back__photo" role="img" aria-label="Photo of a raw beef roast with parsley, rosemary, garlic and sliced carrot"></div>
    <div class="brand-mark">Prime Cuts<br>Market</div>
    <div class="contact">
      <p class="contact__label">Contact:<br>support@primecutsmarket.com.au</p>
      <p class="contact__url">PrimeCutsMarket.com.au</p>
      <div class="contact__social"><span></span><span></span><span></span></div>
    </div>
    <div class="back__stripe">
      <span style="width:84px;background:var(--orange)"></span>
      <span style="width:28px;background:var(--peach)"></span>
      <span style="width:5px;background:var(--orange)"></span>
      <span style="width:11px;background:var(--yellow)"></span>
      <span style="width:14px;background:var(--peach)"></span>
      <span style="width:6px;background:var(--white)"></span>
      <span style="width:41px;background:var(--orange-light)"></span>
      <span style="width:11px;background:var(--orange)"></span>
      <span style="width:15px;background:var(--orange-light)"></span>
      <span style="width:148px;background:var(--peach)"></span>
      <span style="width:20px;background:var(--orange-light)"></span>
      <span style="width:81px;background:var(--green)"></span>
      <span style="width:21px;background:var(--orange-light)"></span>
      <span style="width:11px;background:var(--white)"></span>
      <span style="width:74px;background:var(--orange-light)"></span>
    </div>
  </section>

  <section class="panel cover">
    <svg width="570" height="738" viewBox="0 0 570 738">
      <defs>
        <linearGradient id="band" x1="0" x2="1">
          <stop offset="0" stop-color="#ffc214"/>
          <stop offset=".5" stop-color="#fee18a"/>
          <stop offset="1" stop-color="#ffc214"/>
        </linearGradient>
        <linearGradient id="photo" x1="0" y1="0" x2="0" y2="1">
          <stop offset="0" stop-color="#2a1a12"/>
          <stop offset=".4" stop-color="#a84a44"/>
          <stop offset="1" stop-color="#3a1f14"/>
        </linearGradient>
      </defs>
      <path d="M0,251 Q285,370 570,214 L570,344 Q285,360 0,344 Z" fill="url(#band)"/>
      <path d="M0,300 Q285,360 570,270 L570,320 Q285,350 0,330 Z" fill="#f78f20" opacity=".6"/>
      <path d="M0,485 Q230,370 570,380 L570,500 Q260,430 0,535 Z" fill="#66a12b"/>
      <g role="img" aria-label="Photo of cured hams, salami and sausages on a wooden board">
        <path d="M0,520 Q250,405 570,410 L570,738 L0,738 Z" fill="url(#photo)"/>
      </g>
    </svg>
    <h1 class="cover__title">Buying&nbsp; Meat Made Easy!</h1>
    <p class="cover__url">PrimeCutsMarket.com.au</p>
    <div class="cover__logo">Prime Cuts<br>Market</div>
  </section>
</main>
</body>
</html>
```